Upsell Vertical Banner Ad Design For B2B Marketing Agency Vertical 768px × 1180px IS THE SIZE

I need a banner made for my website www.brightlanepromotionhub.biz This banner will be an upsell advertisement for after someone signs up for my monthly program. When they login to their account for the 1st time I will give them the chance to upgrade their account to our annual program with just one click.

this is a page that upsells it currently to give you an idea how we market ourselves:
https://tlpx.pagevault-example.com/page/tlp-annual-upsell

Use this content:

Are You Ready To Commit To Taking Your Business To The Next Level?

Because We're In This For The Long-Haul and Dedicated To Your Success...

Save $300 By Upgrading To An Annual Membership And Pay Only $74/mth

((BUTTON))Yes, Upgrade My Plan Right Now!

*Must prepay the full year at only $898/yr!

Target Market(s)

business owners

Industry/Entity Type

Marketing

Requirements
Must have
• 768px × 1180px IS THE SIZE vertical

Use this content:

Nice to have
• Use this content:

Should not have
• Use this content:

```html
<!DOCTYPE html>
<html lang="en">
<head>
<meta charset="utf-8">
<title>Bright Lane Promotion Hub – Annual Membership Upgrade</title>
<link rel="stylesheet" href="https://fonts.googleapis.com/css2?family=Archivo+Black&family=Gochi+Hand&family=Montserrat:wght@600;800&display=swap">
<style>
  :root {
    --board-dark: #2b2b2b;
    --board-mid: #3d3d3d;
    --board-light: #4a4a4a;
    --chalk-white: #f2f2f2;
    --chalk-yellow: #f3ec2b;
    --accent-green: #35e06a;
    --offer-green: #1d7a3b;
    --button-green: #169c3a;
    --paper: #ffffff;
    --ink: #111111;
  }
  * { margin: 0; padding: 0; box-sizing: border-box; }
  html, body { width: 781px; height: 1200px; overflow: hidden; background: var(--board-dark); }
  .banner {
    position: relative;
    width: 781px;
    height: 1200px;
    overflow: hidden;
    background: radial-gradient(ellipse at 50% 35%, var(--board-light) 0%, var(--board-mid) 45%, var(--board-dark) 100%);
  }
  .brand {
    position: absolute;
    left: 20px;
    top: 22px;
    display: flex;
    align-items: center;
    gap: 10px;
    color: var(--chalk-white);
    font-family: "Montserrat", sans-serif;
    font-weight: 800;
    font-size: 17px;
    line-height: 1.1;
    letter-spacing: 0.5px;
  }
  .brand-mark { width: 34px; height: 34px; background: var(--chalk-white); }
  .chalk-illustration {
    position: absolute;
    left: 22px;
    top: 92px;
    width: 450px;
    height: 455px;
    background: radial-gradient(ellipse at 55% 45%, #505050 0%, rgba(70,70,70,0.4) 60%, rgba(60,60,60,0) 100%);
  }
  .headline {
    position: absolute;
    right: 38px;
    top: 330px;
    width: 480px;
    text-align: right;
    font-family: "Gochi Hand", cursive;
    font-size: 38px;
    line-height: 42px;
    text-transform: uppercase;
    color: var(--chalk-white);
    letter-spacing: 0.5px;
  }
  .headline .highlight { color: var(--chalk-yellow); }
  .commitment {
    position: absolute;
    left: 0;
    top: 588px;
    width: 781px;
    text-align: center;
    padding: 0 70px;
    font-family: "Archivo Black", sans-serif;
    font-size: 24px;
    line-height: 38px;
    letter-spacing: 0.6px;
    text-transform: uppercase;
    color: var(--accent-green);
  }
  .paper-strip { position: absolute; left: 0; top: 700px; width: 781px; height: 320px; }
  .offer {
    position: absolute;
    left: 0;
    top: 758px;
    width: 781px;
    text-align: center;
    font-family: "Archivo Black", sans-serif;
    color: var(--ink);
  }
  .offer-line { display: block; font-size: 33px; line-height: 50px; letter-spacing: 1.5px; transform: skewX(-6deg); }
  .offer-amount { color: var(--offer-green); font-size: 48px; }
  .offer-line.first { line-height: 58px; }
  .upgrade-button {
    position: absolute;
    left: 104px;
    top: 1054px;
    width: 572px;
    height: 93px;
    border-radius: 16px;
    background: var(--button-green);
    color: var(--chalk-white);
    display: flex;
    align-items: center;
    justify-content: center;
    font-family: "Archivo Black", sans-serif;
    font-size: 22px;
    letter-spacing: 0.4px;
    text-decoration: none;
  }
  .fine-print {
    position: absolute;
    left: 0;
    top: 1168px;
    width: 781px;
    text-align: center;
    font-family: "Montserrat", sans-serif;
    font-weight: 800;
    font-style: italic;
    font-size: 14px;
    color: var(--chalk-white);
  }
</style>
</head>
<body>
<main class="banner">
  <div class="brand"><span class="brand-mark"></span><span>BRIGHT LANE<br>PROMOTION HUB</span></div>

  <div class="chalk-illustration" role="img" aria-label="Chalk drawing of a stick figure climbing stairs toward a glowing light bulb, with an upward arrow"></div>

  <h1 class="headline">
    <span class="highlight">Are you ready</span> to<br>
    commit to taking<br>
    your business to the<br>
    <span class="highlight">next level?</span>
  </h1>

  <p class="commitment">Because we're in this for the long-haul and dedicated to your success...</p>

  <svg class="paper-strip" viewBox="0 0 781 320" aria-hidden="true">
    <polygon fill="var(--paper)" points="0,36 22,30 40,38 62,24 84,32 104,20 126,30 150,22 168,34 190,26 214,36 236,28 258,18 280,28 304,22 326,34 348,24 372,30 396,16 418,26 440,20 462,32 486,24 508,12 530,22 552,14 576,26 600,18 622,28 646,8 668,18 690,10 712,22 736,12 758,20 781,10
      781,272 758,280 736,268 712,276 690,262 668,272 646,266 622,280 600,270 576,284 552,274 530,286 508,276 486,290 462,282 440,294 418,284 396,296 372,288 348,298 326,290 304,300 280,292 258,302 236,294 214,304 190,296 168,306 150,298 126,308 104,300 84,310 62,302 40,312 22,304 0,314"/>
  </svg>

  <p class="offer">
    <span class="offer-line first">Save <span class="offer-amount">$300</span></span>
    <span class="offer-line">by upgrading</span>
    <span class="offer-line">to an annual membership &amp;</span>
    <span class="offer-line">pay only <span class="offer-amount">$74</span>/mth</span>
  </p>

  <a class="upgrade-button" href="https://tlpx.pagevault-example.com/page/tlp-annual-upsell">Yes, Upgrade My Plan Right Now!</a>

  <p class="fine-print">*Must prepay the full year at only $898/yr!</p>
</main>
</body>
</html>
```